Website for Company that serves and supports Investment Banks

We are seeking to have a six page website that provides a basic description of our company's services. Our company provides Financial Models and Investment Memos on an outsourced basis to Small Investment Banks and Investment firms. We do not require a shopping cart. We already have a logo attached.

Target Market(s)

Small, regional investment banks. Small private equity firms.

Industry/Entity Type

Finance And Accounting

Coding

Coded - Design and coding required

Number of Pages Required

5+ page

Requirements
Nice to have
• Please use the logo design to drive how you design the layout for the website

```html
<!DOCTYPE html>
<html lang="en">
<head>
<meta charset="utf-8">
<title>Ledgerpoint Analysts</title>
<link href="https://fonts.googleapis.com/css2?family=Cinzel:wght@400;700&family=Questrial&display=swap" rel="stylesheet">
<style>
:root{
  --navy:#0d2d55;
  --navy-deep:#0a2246;
  --blue:#1d4a86;
  --text:#3b3b3b;
  --paper:#ffffff;
  --footer-bar:#0f2a52;
}
*{margin:0;padding:0;box-sizing:border-box}
html,body{width:1200px;height:3766px;overflow:hidden}
body{font-family:"Questrial",Arial,sans-serif;color:var(--text);background:var(--paper);position:relative}
.abs{position:absolute}

/* hero */
.hero-photo{left:0;top:0;width:1200px;height:640px;background:linear-gradient(135deg,#d9d6d0 0%,#b9b3ab 40%,#8f8a85 70%,#c8c3bc 100%)}
.header{left:75px;top:25px;width:1050px;height:100px;background:rgba(255,255,255,.9);display:flex;align-items:center;padding:0 20px;white-space:nowrap}
.brand{font-family:"Cinzel",Georgia,serif;font-weight:700;font-size:17px;color:var(--navy);display:flex;align-items:center;gap:10px}
.brand-mark{width:32px;height:32px;border-radius:50%;background:var(--navy)}
.nav{display:flex;gap:30px;margin-left:auto;font-size:17px;color:#555}
.nav .active{color:var(--navy);font-weight:bold}
.call{margin-left:60px;display:flex;align-items:center;gap:12px;text-align:right}
.call b{display:block;color:var(--navy);font-size:18px}
.call span{font-size:14px;color:#666}
.call-icon{width:46px;height:46px;border-radius:50%;background:var(--navy);display:flex;align-items:center;justify-content:center}
.hero-title{left:235px;top:298px;width:720px;height:72px;background:rgba(40,70,110,.75);color:#fff;font-family:"Cinzel",Georgia,serif;font-size:44px;text-align:center;line-height:72px;letter-spacing:2px;white-space:nowrap}
.hero-sub{left:160px;top:376px;width:880px;height:80px;background:rgba(20,20,20,.55);color:#fff;font-size:19px;text-align:center;padding:10px 30px;line-height:28px}

.pricing{left:75px;top:628px;width:1050px;height:250px;background:#f4f4f4;box-shadow:0 6px 14px rgba(0,0,0,.2)}
.pricing-tip{left:75px;top:876px;width:1050px;height:56px}
.plan{top:565px;width:240px;text-align:center}
.price{width:116px;height:116px;margin:0 auto;border-radius:50%;background:var(--navy);border:5px solid #fff;box-shadow:0 0 0 2px var(--navy);color:#fff;font-size:30px;font-weight:bold;line-height:106px}
.plan h3{margin-top:20px;font-size:21px;color:var(--navy);line-height:25px;font-weight:bold}
.plan p{margin-top:16px;font-size:15px;line-height:21px;color:#555;padding:0 20px}
.chev{margin-top:18px}

/* headings */
.section-title{left:0;width:1200px;text-align:center;font-family:"Cinzel",Georgia,serif;font-size:42px;color:#333;white-space:nowrap}
.section-title b{color:var(--navy)}
.title-rule{height:1px;background:#bbb}
.welcome-text{left:165px;top:1090px;width:870px;font-size:15px;line-height:26px;color:#555;text-align:center}

/* why hire */
.why{left:0;top:1255px;width:1200px;height:485px;background:linear-gradient(120deg,#1c4a86 0%,#14396c 60%,#1e4c88 100%)}
.why-title{top:1300px;color:#fff}
.why-photo{left:110px;top:1395px;width:440px;height:270px;border:6px solid #fff;background:linear-gradient(135deg,#e6e6e6,#7a7d83 50%,#2e3238)}
.why-text{left:597px;top:1395px;width:500px;color:#fff;font-size:15px;line-height:25px}
.btn-white{left:597px;top:1608px;width:160px;height:56px;background:#fff;color:var(--navy);font-size:19px;font-weight:bold;text-align:center;line-height:56px}

/* process */
.step{display:flex;gap:16px}
.step-num{flex:none;width:46px;height:46px;border-radius:50%;background:var(--navy);color:#fff;font-size:21px;line-height:46px;text-align:center}
.step p{font-size:14.5px;line-height:21px;color:#444;padding-top:4px}
.process-photo{left:850px;top:1900px;width:290px;height:440px;border-radius:40%;background:radial-gradient(ellipse at 50% 50%,#8a8f98 0%,#c9ccd1 55%,#fff 80%)}

/* testimonial */
.quote-band{left:0;top:2480px;width:1200px;height:225px;background:linear-gradient(90deg,#1a3f72,#24508a,#1a3f72)}
.avatar{left:78px;top:2540px;width:105px;height:105px;border-radius:50%;border:4px solid #fff;background:linear-gradient(#c99b7a,#7a5540)}
.quote{left:220px;top:2535px;width:820px;color:#fff;font-size:15px;line-height:27px}
.quote b{display:block;margin-top:4px;font-size:16px;letter-spacing:1px}
.arrow-box{top:2620px;width:28px;height:28px;border:2px solid #fff;display:flex;align-items:center;justify-content:center}

/* blog */
.post{top:2860px;width:250px}
.post-img{height:150px}
.post time{display:block;margin-top:22px;font-size:14px;color:#888}
.post h4{margin-top:10px;font-family:"Cinzel",Georgia,serif;font-size:19px;line-height:25px;color:var(--navy);font-weight:700}
.post hr{border:0;border-top:2px dashed #c6c6c6;margin-top:20px}
.post-meta{margin-top:18px;display:flex;gap:40px;font-size:15px;color:var(--navy)}
.post-meta span{display:flex;align-items:center;gap:8px}

/* footer */
.footer{left:0;top:3283px;width:1200px;height:427px;background:linear-gradient(180deg,#2a2f33,#1b1e21)}
.foot-col{top:3353px;color:#fff}
.foot-col h5{font-family:"Cinzel",Georgia,serif;font-size:22px;font-weight:400;letter-spacing:1px;white-space:nowrap}
.foot-col ul{list-style:none;margin-top:38px;font-size:14.5px;line-height:29px}
.foot-brand{margin-top:50px;display:flex;flex-direction:column;align-items:center;gap:14px;font-family:"Cinzel",Georgia,serif;font-size:15px;font-weight:700;white-space:nowrap}
.foot-brand .brand-mark{width:90px;height:90px;border:3px solid #fff;background:transparent}
.contact{margin-top:36px;font-size:14.5px;line-height:22px}
.contact li{display:flex;gap:12px;margin-bottom:14px}
.contact svg{flex:none;margin-top:3px}
.news p{margin-top:36px;font-size:14.5px;line-height:22px;width:250px}
.email-field{margin-top:16px;width:245px;height:46px;background:#fff;color:#888;font-size:14px;padding:14px 12px}
.submit{margin-top:10px;width:155px;height:50px;background:var(--navy-deep);border:2px solid #fff;color:#fff;font-size:19px;text-align:center;line-height:46px}
.copy-bar{left:0;top:3710px;width:1200px;height:56px;background:var(--footer-bar);color:#fff;font-size:14px;line-height:56px;padding-left:78px}
.social{top:3720px;width:34px;height:34px;border-radius:50%;background:#fff}
</style>
</head>
<body>

<div class="abs hero-photo" role="img" aria-label="Photo of a woman working at a laptop in a bright office"></div>

<header class="abs header">
  <div class="brand"><span class="brand-mark"></span>Ledgerpoint Analysts</div>
  <nav class="nav"><span class="active">Home</span><span>About</span><span>Product</span><span>Why hire</span><span>Process</span><span>Contact</span></nav>
  <div class="call">
    <div><b>555-014-2290</b><span>Call us now</span></div>
    <div class="call-icon"><svg width="22" height="22" viewBox="0 0 24 24"><path fill="#fff" d="M6.6 10.8a15.1 15.1 0 0 0 6.6 6.6l2.2-2.2a1 1 0 0 1 1-.25 11.4 11.4 0 0 0 3.6.6 1 1 0 0 1 1 1V20a1 1 0 0 1-1 1A17 17 0 0 1 3 4a1 1 0 0 1 1-1h3.5a1 1 0 0 1 1 1c0 1.25.2 2.45.6 3.6a1 1 0 0 1-.25 1z"/></svg></div>
  </div>
</header>

<h1 class="abs hero-title">Ledgerpoint Analysts</h1>
<p class="abs hero-sub">Lorem Ipsum is simply dummy text of the printing and typesetting industry. Lorem Ipsum has been the industry's standard dummy text ever since the 1500s.</p>

<div class="abs pricing"></div>
<svg class="abs pricing-tip" viewBox="0 0 1050 56" preserveAspectRatio="none"><polygon points="0,0 1050,0 525,56" fill="#f4f4f4"/></svg>

<div class="abs plan" style="left:85px">
  <div class="price">$3500</div><h3>FINANCIAL<br>MODELS</h3>
  <p>Lorem Ipsum is simply dummy text of the printing and text typesetting industry.</p>
  <svg class="chev" width="30" height="16" viewBox="0 0 30 16"><path d="M3 2l12 6 12-6M3 8l12 6 12-6" stroke="#1d4a86" stroke-width="2" fill="none"/></svg>
</div>
<div class="abs plan" style="left:340px">
  <div class="price">$2500</div><h3>INVESTMENT<br>DOCUMENTS</h3>
  <p>Lorem Ipsum is simply dummy text of the printing and text typesetting industry.</p>
  <svg class="chev" width="30" height="16" viewBox="0 0 30 16"><path d="M3 2l12 6 12-6M3 8l12 6 12-6" stroke="#777" stroke-width="2" fill="none"/></svg>
</div>
<div class="abs plan" style="left:590px">
  <div class="price">$3500</div><h3>VALUATION<br>MODELS</h3>
  <p>Lorem Ipsum is simply dummy text of the printing and text typesetting industry.</p>
  <svg class="chev" width="30" height="16" viewBox="0 0 30 16"><path d="M3 2l12 6 12-6M3 8l12 6 12-6" stroke="#777" stroke-width="2" fill="none"/></svg>
</div>
<div class="abs plan" style="left:840px">
  <div class="price">$500</div><h3>DEAL SUPPORT<br>MEMOS</h3>
  <p>Lorem Ipsum is simply dummy text of the printing and text typesetting industry.</p>
  <svg class="chev" width="30" height="16" viewBox="0 0 30 16"><path d="M3 2l12 6 12-6M3 8l12 6 12-6" stroke="#777" stroke-width="2" fill="none"/></svg>
</div>

<div class="abs title-rule" style="left:110px;top:1050px;width:120px"></div>
<div class="abs title-rule" style="left:970px;top:1050px;width:120px"></div>
<h2 class="abs section-title" style="top:1022px">Welcome to <b>Ledgerpoint</b></h2>
<p class="abs welcome-text">Ledgerpoint Analysts functions as an outsourced Financial Analyst partner for smaller, regional investment banks, private equity firms, business brokers, and mezzanine loan funds. We focus exclusively on lower middle-market clients. We believe Financial Models and Investment Memos are two of the most important deal support tools for executing private equity and investment banking transactions. Ledgerpoint Analysts specializes in delivering robust LBO, Growth Equity, Recap and Merger models.</p>

<section class="abs why"></section>
<h2 class="abs section-title why-title" style="color:#fff">Why Hire Ledgerpoint..!</h2>
<div class="abs why-photo" role="img" aria-label="Overhead photo of business people meeting around a table"></div>
<p class="abs why-text">We are much more cost-effective than hiring full-time Analyst pool. We give you the ability to purchase Financial Models and Investment Memos on a "product-by-product" on demand basis with standardized prices. Cost of our Financial Models and Investment Memos is less expensive than other outsourced deal providers including investment bankers, attorneys, accountants and industry consultants. Cost of our Financial Models and Investment Memos is less expensive than Quality of Earnings Analysis.</p>
<div class="abs btn-white">READ MORE</div>

<div class="abs title-rule" style="left:300px;top:1822px;width:110px"></div>
<div class="abs title-rule" style="left:790px;top:1822px;width:110px"></div>
<h2 class="abs section-title" style="top:1794px">Finance <b>Process</b></h2>

<div class="abs step" style="left:78px;top:1910px;width:250px"><div class="step-num">1</div><p>Call or email us a brief two sentence description of your deal project and indicate whether you are interested in our Financial Model or Investment Memo products.</p></div>
<div class="abs step" style="left:360px;top:1910px;width:225px"><div class="step-num">2</div><p>A Ledgerpoint client service rep will contact you within 24 hours</p></div>
<div class="abs step" style="left:615px;top:1910px;width:215px"><div class="step-num">3</div><p>To ensure confidentiality, we will request that you forward a copy of your Non-Disclosure Agreement for our execution.</p></div>
<div class="abs step" style="left:78px;top:2078px;width:300px"><div class="step-num">4</div><p>In order for us to get our arms around the transaction we will email you a blank Sources &amp; Uses of Funds template. We will request that you populate this template with all necessary "Flow-of-Funds" information for your transaction.</p></div>
<div class="abs step" style="left:480px;top:2078px;width:345px"><div class="step-num">5</div><p>You email us all of the basic information we would need to create your Financial Model including historical financials, internal management projections, any relevant depreciation, amortization or debt paydown schedules as well as information about the terms of each tranche of debt.</p></div>
<div class="abs step" style="left:78px;top:2258px;width:300px"><div class="step-num">6</div><p>You email us all of the basic information we would need to create your Investment Memo including internal Company Overview documents, internal industry information, management team bios, relevant website content, and any relevant strategic planning documents.</p></div>
<div class="abs step" style="left:480px;top:2258px;width:330px"><div class="step-num">6</div><p>We email You a completed Financial Model or Investment Memo within 72 hours.</p></div>

<div class="abs process-photo" role="img" aria-label="Photo of a cheering businessman in a grey suit jumping"></div>

<section class="abs quote-band" role="img" aria-label="Blue tinted crowd background"></section>
<div class="abs avatar" role="img" aria-label="Client portrait"></div>
<p class="abs quote">Lorem Ipsum is simply dummy text of the printing and typesetting industry. Lorem Ipsum has been the industry's standard dummy text ever since the 1500s, when an unknown printer took a galley of type and scrambled it to make a type specimen book.<b>OWEN T.</b></p>
<div class="abs arrow-box" style="left:1020px"><svg width="12" height="12" viewBox="0 0 12 12"><path d="M8 1L3 6l5 5z" fill="#fff"/></svg></div>
<div class="abs arrow-box" style="left:1052px"><svg width="12" height="12" viewBox="0 0 12 12"><path d="M4 1l5 5-5 5z" fill="#fff"/></svg></div>

<div class="abs title-rule" style="left:330px;top:2790px;width:120px"></div>
<div class="abs title-rule" style="left:750px;top:2790px;width:120px"></div>
<h2 class="abs section-title" style="top:2762px">Recent <b>Blog</b></h2>

<article class="abs post" style="left:78px">
  <div class="post-img" role="img" aria-label="Photo of banknotes and a calculator" style="background:linear-gradient(135deg,#c9a46a,#8a7aa8 50%,#d6c8b0)"></div>
  <time>Posted at 18 December 2017</time>
  <h4>Lorem Ipsum dummy typesetting industry.</h4><hr>
  <div class="post-meta"><span><svg width="16" height="16" viewBox="0 0 16 16"><circle cx="8" cy="5" r="4" fill="#0d2d55"/><path d="M0 16a8 6 0 0 1 16 0z" fill="#0d2d55"/></svg>admin</span><span><svg width="16" height="16" viewBox="0 0 16 16"><path d="M2 2h12v9H6l-4 3z" fill="none" stroke="#0d2d55" stroke-width="2"/></svg>1 comment</span></div>
</article>
<article class="abs post" style="left:343px">
  <div class="post-img" role="img" aria-label="Photo of two businessmen shaking hands" style="background:linear-gradient(135deg,#e8e8e8,#6f7680 55%,#cfd2d6)"></div>
  <time>Posted at 18 December 2017</time>
  <h4>Lorem Ipsum dummy typesetting industry.</h4><hr>
  <div class="post-meta" style="color:#888"><span><svg width="16" height="16" viewBox="0 0 16 16"><circle cx="8" cy="5" r="4" fill="#888"/><path d="M0 16a8 6 0 0 1 16 0z" fill="#888"/></svg>admin</span><span><svg width="16" height="16" viewBox="0 0 16 16"><path d="M2 2h12v9H6l-4 3z" fill="none" stroke="#888" stroke-width="2"/></svg>1 comment</span></div>
</article>
<article class="abs post" style="left:608px">
  <div class="post-img" role="img" aria-label="Photo of a rising growth chart" style="background:linear-gradient(135deg,#0e2a4a,#1f5d7a 55%,#6ea7b8)"></div>
  <time>Posted at 18 December 2017</time>
  <h4>Lorem Ipsum dummy typesetting industry.</h4><hr>
  <div class="post-meta" style="color:#888"><span><svg width="16" height="16" viewBox="0 0 16 16"><circle cx="8" cy="5" r="4" fill="#888"/><path d="M0 16a8 6 0 0 1 16 0z" fill="#888"/></svg>admin</span><span><svg width="16" height="16" viewBox="0 0 16 16"><path d="M2 2h12v9H6l-4 3z" fill="none" stroke="#888" stroke-width="2"/></svg>1 comment</span></div>
</article>
<article class="abs post" style="left:873px">
  <div class="post-img" role="img" aria-label="Photo of an adviser meeting an older couple" style="background:linear-gradient(135deg,#eeeae4,#a8a099 55%,#dcd6ce)"></div>
  <time>Posted at 18 December 2017</time>
  <h4>Lorem Ipsum dummy typesetting industry.</h4><hr>
  <div class="post-meta" style="color:#888"><span><svg width="16" height="16" viewBox="0 0 16 16"><circle cx="8" cy="5" r="4" fill="#888"/><path d="M0 16a8 6 0 0 1 16 0z" fill="#888"/></svg>admin</span><span><svg width="16" height="16" viewBox="0 0 16 16"><path d="M2 2h12v9H6l-4 3z" fill="none" stroke="#888" stroke-width="2"/></svg>1 comment</span></div>
</article>

<footer class="abs footer" role="img" aria-label="Dark background photo of business silhouettes shaking hands"></footer>
<div class="abs foot-col" style="left:140px">
  <h5>About Us</h5>
  <div class="foot-brand" style="margin-left:-20px;width:200px"><span class="brand-mark"></span>Ledgerpoint Analysts</div>
  <p style="margin-top:20px;font-size:14.5px;line-height:21px;width:210px">Lorem Ipsum is simply dummy text of the printing and typesetting industry.</p>
</div>
<div class="abs foot-col" style="left:375px">
  <h5>Useful Links</h5>
  <ul><li>Home</li><li>About</li><li>Product</li><li>Why hire</li><li>Process</li><li>Contact</li></ul>
</div>
<div class="abs foot-col" style="left:580px">
  <h5>Get in touch</h5>
  <ul class="contact" style="list-style:none">
    <li><svg width="16" height="20" viewBox="0 0 16 20"><path d="M8 0a7 7 0 0 1 7 7c0 5-7 13-7 13S1 12 1 7a7 7 0 0 1 7-7z" fill="#fff"/><circle cx="8" cy="7" r="2.5" fill="#222"/></svg><span><b>Ledgerpoint Analysts</b><br>12 Harbour Row, Eastvale,<br>EV4 2QR</span></li>
    <li><svg width="16" height="16" viewBox="0 0 24 24"><path fill="#fff" d="M6.6 10.8a15.1 15.1 0 0 0 6.6 6.6l2.2-2.2a1 1 0 0 1 1-.25 11.4 11.4 0 0 0 3.6.6 1 1 0 0 1 1 1V20a1 1 0 0 1-1 1A17 17 0 0 1 3 4a1 1 0 0 1 1-1h3.5a1 1 0 0 1 1 1c0 1.25.2 2.45.6 3.6a1 1 0 0 1-.25 1z"/></svg>555-014-2290</li>
    <li><svg width="16" height="14" viewBox="0 0 16 12"><rect width="16" height="12" fill="#fff"/><path d="M0 0l8 6 8-6" stroke="#222" fill="none"/></svg>hello@ledgerpointanalysts.example</li>
    <li><svg width="16" height="16" viewBox="0 0 16 16"><circle cx="8" cy="8" r="7" stroke="#fff" stroke-width="1.5" fill="none"/><path d="M1 8h14M8 1c-3 4-3 10 0 14M8 1c3 4 3 10 0 14" stroke="#fff" fill="none"/></svg>www.ledgerpointanalysts.example</li>
  </ul>
</div>
<div class="abs foot-col news" style="left:872px">
  <h5>Newsletter</h5>
  <p>Would you like to receive exclusive access to articles, white papers and our regular monthly newsletter?</p>
  <div class="email-field">Enter Email Id</div>
  <div class="submit">SUBMIT</div>
</div>

<div class="abs copy-bar">copyright | Ledgerpoint Analysts - 2017 All Right Reserved</div>
<div class="abs social" style="left:982px"></div>
<div class="abs social" style="left:1020px"></div>
<div class="abs social" style="left:1058px"></div>
<div class="abs social" style="left:1096px"></div>

</body>
</html>
```